B2B Website for manufacturer of aerospace coatings

B2B Website for manufacturer of aerospace optical coatings and screens used in flight simulators and air-traffic controller centers. We sell to both the military as well as commercial airlines.

Colors: primary colors should be white and blue (same blue as in the logo), but you can accent with red, orange, or any other colors.

Main menu: Products, Services, About Us, Contact Us

Logo = See "Halden SkyLumen" JPEG attached.

We'd like a professional website that appeals to engineers at companies like Varnett, QORV, the military, etc.

We intend to build this website on WordPress.

Websites we like in our industry:
https://www.plexomirra.com/
https://www.dwo.com/civil-aviation/aviation-simulation-equipment/training-equipment/full-flight-simulators/
https://z7services.com/
https://www.lumbrexno.com/
https://kelvarnpq.com/
https://glimmerbayworks.com/

3 Pages: Homepage, Product page, Contact Us page

Target Market(s)

Varnett, Prescott Vayle, Corvane

Industry/Entity Type

Aerospace

Number of Pages Required

3 page

Colors
0054AA
0677BA
7BADD7
CADEEF
E8F1F8
F0912C
F2A743
F7CA91
FBE8D2
FDF5EE
EB3D1F
EC4F4E
F09395
F8D3D4
FCEDEE

Requirements
Should not have
• Black background

```html
<!DOCTYPE html>
<html lang="en">
<head>
<meta charset="utf-8">
<title>Halden SkyLumen — Aerospace Optical Screens</title>
<link href="https://fonts.googleapis.com/css2?family=Michroma&family=Barlow:wght@400;500;600;700&display=swap" rel="stylesheet">
<style>
:root{
  --blue:#0054AA;
  --blue-mid:#0677BA;
  --blue-light:#7BADD7;
  --blue-pale:#E8EEF6;
  --orange:#F0912C;
  --orange-deep:#F28A0C;
  --ink:#222831;
  --grey:#555c66;
  --white:#ffffff;
}
*{margin:0;padding:0;box-sizing:border-box}
html,body{width:1200px;height:3632px;overflow:hidden}
body{position:relative;background:var(--white);font-family:"Barlow",sans-serif;color:var(--ink)}
.abs{position:absolute}
.display{font-family:"Michroma",sans-serif;text-transform:uppercase}

/* header */
.site-header{left:0;top:0;width:1200px;height:79px;background:var(--white)}
.brand{left:113px;top:6px;color:var(--blue);font-weight:700;font-size:30px;line-height:30px;letter-spacing:.5px}
.brand small{display:block;font-size:27px;font-weight:700;line-height:30px}
.main-nav a{position:absolute;top:27px;font-size:15px;color:var(--ink);text-decoration:none;letter-spacing:.5px}
.main-nav a.active{color:var(--blue);font-weight:700;border-bottom:3px solid var(--blue);padding-bottom:6px}
.header-phone{left:950px;top:23px;color:var(--blue);font-weight:700;font-size:17px;display:flex;gap:6px;align-items:center}

/* hero */
.hero{left:0;top:79px;width:1200px;height:712px;overflow:hidden}
.hero-photo{position:absolute;inset:0;background:linear-gradient(90deg,#0b5cb3 0%,#1466bf 30%,#2f4f7a 55%,#23304a 75%,#3a3040 100%)}
.hero-glow{position:absolute;inset:0;background:linear-gradient(180deg,rgba(240,145,44,0) 18%,rgba(240,145,44,.35) 30%,rgba(20,30,60,0) 42%)}
.hero-kicker{left:127px;top:262px;color:var(--white);font-size:19px;letter-spacing:3px}
.hero-title{left:124px;top:290px;color:var(--white);font-size:50px;line-height:52px}
.hero-title b{display:block;font-family:"Barlow",sans-serif;font-style:italic;font-weight:700;font-size:62px;letter-spacing:2px}
.hero-text{left:128px;top:412px;width:480px;color:var(--white);font-size:19px;line-height:25px}
.btn{display:flex;align-items:center;justify-content:center;background:var(--orange-deep);color:var(--white);font-weight:700;font-size:14px;letter-spacing:1px;text-decoration:none}
.hero-btn{left:124px;top:488px;width:190px;height:54px;border-radius:27px}
.scroll-cue{left:1160px;top:218px;width:20px;height:236px}
.scroll-cue span{position:absolute;left:-38px;top:100px;transform:rotate(-90deg);color:var(--white);font-size:11px;letter-spacing:2px;white-space:nowrap;font-weight:600}
.scroll-cue i{position:absolute;left:9px;width:2px;height:58px;background:var(--white)}
.hero-curve{left:0;top:680px}
.down-btn{left:579px;top:697px;width:66px;height:66px;border-radius:50%;background:var(--white);box-shadow:0 2px 8px rgba(0,0,0,.15);display:flex;align-items:center;justify-content:center}

/* section headings */
.section-title{left:0;width:1200px;text-align:center;font-size:25px;letter-spacing:1px;color:var(--grey)}
.section-title em{font-style:normal;color:var(--blue)}
.rule{height:3px;background:var(--grey)}

/* products */
.product{width:240px;text-align:center}
.product-photo{width:240px;height:240px;border-radius:50%;border:3px solid var(--blue-light);padding:5px;background-clip:content-box}
.product h3{margin-top:18px;font-size:14px;font-weight:700}
.product p{font-size:13px;line-height:15px;color:var(--grey);margin-top:2px}
.slider-arrow{color:var(--blue)}

/* about */
.about{left:0;top:1344px;width:1200px;height:634px;background:var(--blue-pale)}
.about-kicker{left:647px;top:1453px;font-size:13px;letter-spacing:2px;color:var(--grey)}
.about-title{left:647px;top:1478px;font-size:25px;line-height:31px;color:var(--blue)}
.about-title span{color:var(--grey)}
.about-text{left:647px;width:480px;font-size:18px;line-height:25px;color:var(--ink)}
.about-btn{left:649px;top:1796px;width:182px;height:47px}

/* services */
.service-photo{width:317px;height:317px}
.service-card{width:283px;height:152px;background:var(--white);border-bottom:4px solid var(--blue);box-shadow:0 3px 10px rgba(0,0,0,.08);text-align:center}
.service-card h3{margin-top:52px;font-size:18px;font-weight:600}
.service-card p{font-size:12.5px;line-height:17px;color:var(--grey);margin-top:4px;padding:0 28px}
.service-card a{display:inline-block;margin-top:6px;font-size:12px;font-weight:700;color:var(--orange);text-decoration:underline}
.service-icon{width:60px;height:60px;border-radius:50%;background:var(--blue);border:4px solid var(--white);display:flex;align-items:center;justify-content:center}

/* contact */
.contact{left:0;top:2651px;width:1200px;height:602px;background:linear-gradient(100deg,#0a5ab8 0%,#0b63c2 45%,#0d5cb0 70%,#1a5aa8 100%)}
.contact-kicker{left:93px;top:2792px;font-size:17px;color:var(--white);letter-spacing:.5px}
.contact-title{left:93px;top:2822px;font-size:25px;line-height:30px;color:var(--white)}
.contact-rule{left:95px;top:2887px;width:90px;height:3px;background:var(--white)}
.contact-icon{width:46px;height:46px;border-radius:50%;background:var(--white);display:flex;align-items:center;justify-content:center}
.contact-label{color:var(--white);font-size:18px}
.contact-value{color:var(--white);font-size:24px;font-weight:700}
.contact-value.light{font-weight:400}
.quote-title{left:582px;top:2797px;font-size:17px;color:var(--white);letter-spacing:1px}
.field{height:47px;border:1.5px solid var(--white);color:var(--white);font-size:13.5px;display:flex;align-items:center;gap:8px;padding-left:16px}
.field.message{align-items:flex-start;padding-top:14px;padding-left:20px}
.send-btn{left:588px;top:3055px;width:171px;height:49px;border-radius:25px;font-size:15px}

/* footer */
.footer-brand{left:122px;top:3340px;color:var(--blue);font-weight:700;font-size:30px;line-height:30px}
.footer-about{left:122px;top:3418px;width:270px;font-size:13px;line-height:15px;color:var(--grey)}
.footer-divider{width:1px;height:212px;background:#e2e6ea;top:3285px}
.footer-col h4{font-size:14px;font-weight:700;color:var(--ink);border-left:3px solid var(--blue);padding-left:18px;letter-spacing:.5px}
.footer-col a,.footer-col p{display:block;font-size:14px;color:var(--ink);text-decoration:none;margin-top:12px;padding-left:21px}
.footer-contact p{display:flex;gap:10px;align-items:center;font-size:13.5px;line-height:20px;padding-left:20px}
.pin{width:28px;height:28px;border-radius:50%;background:var(--blue);display:flex;align-items:center;justify-content:center;flex:none}
.footer-base{left:0;top:3550px;width:1170px;height:1px;background:#e2e6ea}
.copyright{left:0;top:3568px;width:1200px;text-align:center;font-size:12.5px;color:var(--grey)}
.copyright u{color:var(--ink)}
</style>
</head>
<body>

<header class="site-header abs">
  <div class="brand abs">Halden<small>SkyLumen</small></div>
  <nav class="main-nav">
    <a class="active" href="#" style="left:345px">HOME</a>
    <a href="#" style="left:436px">PRODUCTS</a>
    <a href="#" style="left:567px">SERVICES</a>
    <a href="#" style="left:689px">ABOUT US</a>
    <a href="#" style="left:811px">CONTACT US</a>
  </nav>
  <div class="header-phone abs">
    <svg width="20" height="20" viewBox="0 0 24 24"><path d="M6.6 10.8a15 15 0 006.6 6.6l2.2-2.2c.3-.3.7-.4 1-.2 1.1.4 2.3.6 3.6.6.6 0 1 .4 1 1V20c0 .6-.4 1-1 1A17 17 0 013 4c0-.6.4-1 1-1h3.5c.6 0 1 .4 1 1 0 1.3.2 2.5.6 3.6.1.3 0 .7-.2 1z" fill="#0054AA"/></svg>
    (123) 456 7890
  </div>
</header>

<section class="hero abs">
  <div class="hero-photo" role="img" aria-label="Cockpit view of a flight deck at dusk with glowing instrument panels"></div>
  <div class="hero-glow"></div>
</section>
<p class="hero-kicker abs display">Welcome to</p>
<h1 class="hero-title abs display">Halden<b>SKYLUMEN</b></h1>
<p class="hero-text abs">Lorem ipsum dolor sit amet, consectetur adipiscing elit, sed do eiusmod tempor incididunt ut.</p>
<a class="btn hero-btn abs" href="#">LEARN MORE ›</a>
<div class="scroll-cue abs"><i style="top:0"></i><span>‹ SCROLL DOWN</span><i style="top:178px"></i></div>
<svg class="hero-curve abs" width="1200" height="112" viewBox="0 0 1200 112">
  <path d="M0 112 L0 108 Q560 20 1200 100 L1200 112 Z" fill="#fff"/>
  <path d="M70 102 Q560 30 1200 100" stroke="#0054AA" stroke-width="5" fill="none"/>
</svg>
<div class="down-btn abs">
  <svg width="26" height="26" viewBox="0 0 24 24"><path d="M12 3v17M5 13l7 7 7-7" stroke="#0054AA" stroke-width="2" fill="none"/></svg>
</div>

<h2 class="section-title abs display" style="top:838px"><em>Feaured</em> Products</h2>
<div class="rule abs" style="left:598px;top:883px;width:48px"></div>
<svg class="slider-arrow abs" style="left:73px;top:1044px" width="20" height="34" viewBox="0 0 20 34"><path d="M17 3L4 17l13 14" stroke="#7BADD7" stroke-width="4" fill="none"/></svg>
<svg class="slider-arrow abs" style="left:1120px;top:1044px" width="20" height="34" viewBox="0 0 20 34"><path d="M3 3l13 14L3 31" stroke="#0054AA" stroke-width="4" fill="none"/></svg>

<div class="product abs" style="left:113px;top:930px">
  <div class="product-photo" role="img" aria-label="White full-motion flight simulator pod on hydraulic legs" style="background-color:#c9d0d8"></div>
  <h3>SED UT PERSPICIATIS</h3><p>Lorem ipsum dolor sit<br>amet consectetur</p>
</div>
<div class="product abs" style="left:364px;top:930px">
  <div class="product-photo" role="img" aria-label="Large curved projection screen interior with a lift platform" style="background-color:#8d99ab"></div>
  <h3>SED UT PERSPICIATIS</h3><p>Lorem ipsum dolor sit<br>amet consectetur</p>
</div>
<div class="product abs" style="left:615px;top:930px">
  <div class="product-photo" role="img" aria-label="Faceted simulator display enclosure with cockpit seat" style="background-color:#7b7f86"></div>
  <h3>SED UT PERSPICIATIS</h3><p>Lorem ipsum dolor sit<br>amet consectetur</p>
</div>
<div class="product abs" style="left:866px;top:930px">
  <div class="product-photo" role="img" aria-label="Military training simulator with terrain projection" style="background-color:#6b7a68"></div>
  <h3>SED UT PERSPICIATIS</h3><p>Lorem ipsum dolor sit<br>amet consectetur</p>
</div>

<section class="about abs"></section>
<svg class="abs" style="left:0;top:1344px" width="660" height="634" viewBox="0 0 660 634" role="img" aria-label="Air traffic control tower simulator with operators at consoles facing a panoramic airport projection">
  <defs><linearGradient id="towerTone" x1="0" y1="0" x2="0" y2="1"><stop offset="0" stop-color="#3d4350"/><stop offset=".35" stop-color="#8f9aa3"/><stop offset=".55" stop-color="#4a4f55"/><stop offset="1" stop-color="#1f2226"/></linearGradient></defs>
  <path d="M0 0H445Q640 300 435 634H0Z" fill="url(#towerTone)"/>
  <path d="M455 0Q660 317 440 634" stroke="#0054AA" stroke-width="6" fill="none"/>
</svg>
<p class="about-kicker abs display">Our company</p>
<h2 class="about-title abs display">About Halden<br><span>SkyLumen</span></h2>
<p class="about-text abs" style="top:1578px">Since Halden Lumaworks’s founding in 1947, Halden has always been considered an optical house first that also happens to manufacture the world’s largest “Seamless” front and back projection screens.</p>
<p class="about-text abs" style="top:1709px">Our mission has always been to provide the highest image fidelity to every project we undertake.</p>
<a class="btn about-btn abs" href="#">LEARN MORE ›</a>

<p class="section-title abs display" style="top:2046px;font-size:13px;letter-spacing:2px">What we do</p>
<h2 class="section-title abs display" style="top:2068px"><em>Our</em> Services</h2>
<div class="abs" style="left:576px;top:2108px;width:44px;height:3px;background:var(--blue)"></div>
<svg class="abs" style="left:42px;top:2310px" width="30" height="62" viewBox="0 0 30 62"><path d="M27 2L3 31l24 29" stroke="#333" stroke-width="2" fill="none"/></svg>
<svg class="abs" style="left:1128px;top:2310px" width="30" height="62" viewBox="0 0 30 62"><path d="M3 2l24 29L3 60" stroke="#333" stroke-width="2" fill="none"/></svg>

<div class="service-photo abs" style="left:103px;top:2155px;background:linear-gradient(160deg,#0b2f7a,#1d5fd1 60%,#0a1c4a)" role="img" aria-label="Control centre with a wall of blue monitoring screens"></div>
<div class="service-photo abs" style="left:443px;top:2155px;background:linear-gradient(160deg,#b88757,#9a6a3c 60%,#6e4a28)" role="img" aria-label="Technician inside a large curved screen frame under construction"></div>
<div class="service-photo abs" style="left:783px;top:2155px;background:linear-gradient(160deg,#9aa0a8,#6d7279 60%,#3e4247)" role="img" aria-label="Simulator display enclosure being relocated"></div>

<div class="service-card abs" style="left:120px;top:2397px"><h3>TRAINING SERVICE</h3><p>Lorem ipsum dolor sit amet, consect-etur adipiscing elit, sed do</p><a href="#">LEARN MORE</a></div>
<div class="service-card abs" style="left:460px;top:2397px"><h3>AVIATION SIMULATON</h3><p>Lorem ipsum dolor sit amet, consect-etur adipiscing elit, sed do</p><a href="#">LEARN MORE</a></div>
<div class="service-card abs" style="left:800px;top:2397px"><h3>RELOCATION</h3><p>Lorem ipsum dolor sit amet, consect-etur adipiscing elit, sed do</p><a href="#">LEARN MORE</a></div>

<div class="service-icon abs" style="left:232px;top:2370px"><svg width="28" height="22" viewBox="0 0 28 22"><rect x="1" y="1" width="26" height="16" fill="none" stroke="#fff" stroke-width="1.6"/><path d="M5 13l5-5 4 3 6-6M9 21h10" stroke="#fff" stroke-width="1.6" fill="none"/></svg></div>
<div class="service-icon abs" style="left:571px;top:2370px"><svg width="28" height="28" viewBox="0 0 28 28"><circle cx="14" cy="14" r="11" fill="none" stroke="#fff" stroke-width="1.6"/><path d="M5 12h18M14 12v10" stroke="#fff" stroke-width="1.6"/></svg></div>
<div class="service-icon abs" style="left:911px;top:2370px"><svg width="28" height="28" viewBox="0 0 28 28"><circle cx="14" cy="14" r="11" fill="none" stroke="#fff" stroke-width="1.6"/><path d="M3 14h22M14 3c5 4 5 18 0 22M14 3c-5 4-5 18 0 22" stroke="#fff" stroke-width="1.4" fill="none"/></svg></div>

<section class="contact abs" role="img" aria-label="Blue-toned cockpit instrument panel backdrop"></section>
<p class="contact-kicker abs">GET IN TOUCH WITH US</p>
<h2 class="contact-title abs display">Contact us<br>today</h2>
<div class="contact-rule abs"></div>
<div class="contact-icon abs" style="left:94px;top:2927px"><svg width="22" height="22" viewBox="0 0 24 24"><path d="M6.6 10.8a15 15 0 006.6 6.6l2.2-2.2c.3-.3.7-.4 1-.2 1.1.4 2.3.6 3.6.6.6 0 1 .4 1 1V20c0 .6-.4 1-1 1A17 17 0 013 4c0-.6.4-1 1-1h3.5c.6 0 1 .4 1 1 0 1.3.2 2.5.6 3.6.1.3 0 .7-.2 1z" fill="#0054AA"/></svg></div>
<p class="contact-label abs" style="left:152px;top:2925px">Phone Number</p>
<p class="contact-value abs" style="left:152px;top:2948px">+47 900 41 266</p>
<div class="contact-icon abs" style="left:94px;top:3004px"><svg width="22" height="16" viewBox="0 0 22 16"><rect x="1" y="1" width="20" height="14" fill="#0054AA"/><path d="M1 1l10 8 10-8" stroke="#fff" stroke-width="1.5" fill="none"/></svg></div>
<p class="contact-label abs" style="left:152px;top:3000px">Write Email us</p>
<p class="contact-value light abs" style="left:152px;top:3023px">contact@haldenskylumen.com</p>

<h3 class="quote-title abs display">Request a quote</h3>
<div class="field abs" style="left:584px;top:2838px;width:261px"><svg width="14" height="14" viewBox="0 0 14 14"><circle cx="7" cy="4" r="3.2" fill="#fff"/><path d="M1 14c0-4 3-6 6-6s6 2 6 6z" fill="#fff"/></svg>First name</div>
<div class="field abs" style="left:856px;top:2838px;width:261px"><svg width="14" height="14" viewBox="0 0 14 14"><circle cx="7" cy="4" r="3.2" fill="#fff"/><path d="M1 14c0-4 3-6 6-6s6 2 6 6z" fill="#fff"/></svg>Last name</div>
<div class="field abs" style="left:584px;top:2893px;width:261px"><svg width="14" height="14" viewBox="0 0 24 24"><path d="M6.6 10.8a15 15 0 006.6 6.6l2.2-2.2c.3-.3.7-.4 1-.2 1.1.4 2.3.6 3.6.6.6 0 1 .4 1 1V20c0 .6-.4 1-1 1A17 17 0 013 4c0-.6.4-1 1-1h3.5c.6 0 1 .4 1 1 0 1.3.2 2.5.6 3.6.1.3 0 .7-.2 1z" fill="#fff"/></svg>Phone number</div>
<div class="field abs" style="left:856px;top:2893px;width:261px"><svg width="15" height="11" viewBox="0 0 22 16"><rect x="1" y="1" width="20" height="14" fill="#fff"/><path d="M1 1l10 8 10-8" stroke="#0a5ab8" stroke-width="2" fill="none"/></svg>Email address</div>
<div class="field message abs" style="left:584px;top:2951px;width:535px;height:84px">Message</div>
<a class="btn send-btn abs" href="#">SEND NOW</a>

<div class="footer-brand abs">Halden<br>SkyLumen</div>
<p class="footer-about abs">Lorem ipsum dolor sit amet, consectetur adipiscing elit, sed do eiusmod tempor incididunt ut labore et dolore</p>
<div class="footer-divider abs" style="left:444px"></div>
<div class="footer-divider abs" style="left:670px"></div>
<div class="footer-divider abs" style="left:864px"></div>
<div class="footer-col abs" style="left:445px;top:3341px"><h4>NAVIGATION</h4><a href="#">Home</a><a href="#">About Us</a><a href="#">Services</a><a href="#">Products</a></div>
<div class="footer-col abs" style="left:671px;top:3341px"><h4>RESOURCES</h4><a href="#" style="margin-top:16px">Terms of Use</a><a href="#">Privacy Policy</a><a href="#">Contact Us</a></div>
<div class="footer-col footer-contact abs" style="left:865px;top:3341px"><h4>CONTACT US</h4>
  <p style="margin-top:12px"><span class="pin"><svg width="12" height="14" viewBox="0 0 12 14"><path d="M6 0a5 5 0 00-5 5c0 4 5 9 5 9s5-5 5-9a5 5 0 00-5-5z" fill="#fff"/><circle cx="6" cy="5" r="2" fill="#0054AA"/></svg></span>123 Address line here<br>City Country Lorem ipsum</p>
  <p><span class="pin"><svg width="13" height="13" viewBox="0 0 24 24"><path d="M6.6 10.8a15 15 0 006.6 6.6l2.2-2.2c.3-.3.7-.4 1-.2 1.1.4 2.3.6 3.6.6.6 0 1 .4 1 1V20c0 .6-.4 1-1 1A17 17 0 013 4c0-.6.4-1 1-1h3.5c.6 0 1 .4 1 1 0 1.3.2 2.5.6 3.6.1.3 0 .7-.2 1z" fill="#fff"/></svg></span>+123 456 7890</p>
  <p><span class="pin"><svg width="13" height="10" viewBox="0 0 22 16"><rect x="1" y="1" width="20" height="14" fill="#fff"/><path d="M1 1l10 8 10-8" stroke="#0054AA" stroke-width="2" fill="none"/></svg></span>info@haldenskylumen.com</p>
</div>
<div class="footer-base abs"></div>
<p class="copyright abs">© 2022 <u>Halden SkyLumen</u> All Rights Reserved</p>

</body>
</html>
```